Dr Delwyn's Letterhead

I need a professional neat letterhead incorporating my professional information, university titles and qualifications. I have attached my 3 recent ones which contain all the necessary information that needs to be included. I am happy for the information to be a side bar left or right, or as a header/footer combination.

Hello all

I have now made a 2nd and 3rd prize so please submit

Reason: Now there is a 2nd and 3rd place so I can take 3 designs

University

```html
<!DOCTYPE html>
<html lang="en">
<head>
<meta charset="utf-8">
<title>Dr. Tariq Delwyn – Letterhead</title>
<link rel="stylesheet" href="https://fonts.googleapis.com/css2?family=Orbitron:wght@400&family=Oswald:wght@300&display=swap">
<style>
  :root {
    --paper: #ffffff;
    --deep: #2a8fbb;
    --ocean: #23a9c9;
    --aqua: #29c2d6;
    --mist: #dcebf3;
    --rule: #1fbdd3;
    --rule-soft: #a8e6ef;
    --ink: #1b2a33;
    --contact: #2bb5cf;
  }
  * { margin: 0; padding: 0; box-sizing: border-box; }
  html, body { width: 927px; height: 1200px; overflow: hidden; background: var(--paper); }
  .letterhead { position: relative; width: 927px; height: 1200px; background: var(--paper); overflow: hidden; }

  .header-band {
    position: absolute; left: 0; top: 0; width: 927px; height: 210px;
    background: linear-gradient(90deg, var(--deep) 0%, var(--ocean) 45%, var(--aqua) 68%, #bfeaf2 74%, var(--paper) 77%);
  }
  .name-plate-box {
    position: absolute; left: 0; top: 18px; width: 467px; height: 46px;
    background: rgba(255,255,255,0.42);
  }
  .address-rule { position: absolute; left: 706px; top: 206px; width: 200px; height: 3px; background: var(--rule); }
  .header-rule { position: absolute; left: 0; top: 211px; width: 927px; height: 3px; background: var(--rule-soft); }

  .name-plate {
    position: absolute; left: 50px; top: 19px;
    font-family: "Orbitron", sans-serif; font-weight: 400; font-size: 34px;
    color: #ffffff; letter-spacing: 1px; line-height: 44px; white-space: nowrap;
  }
  .credentials {
    position: absolute; left: 52px; top: 74px; list-style: none;
    font-family: "Oswald", sans-serif; font-weight: 300; font-size: 14.5px;
    line-height: 22.5px; color: var(--ink); white-space: nowrap;
  }
  .practice-addresses {
    position: absolute; right: 34px; top: 64px; list-style: none; text-align: right;
    font-family: "Oswald", sans-serif; font-weight: 300; font-size: 14.5px;
    line-height: 25.5px; color: var(--contact); white-space: nowrap;
  }

  .footer-band {
    position: absolute; left: 0; top: 1000px; width: 927px; height: 200px;
    background: linear-gradient(180deg, rgba(220,235,243,0) 0%, rgba(205,230,242,0.7) 55%, #c8dfee 100%);
  }
</style>
</head>
<body>
<div class="letterhead">
  <div class="header-band" role="img" aria-label="Abstract decorative header in blue and aqua tones"></div>
  <div class="name-plate-box"></div>
  <div class="address-rule"></div>
  <div class="header-rule"></div>

  <div class="name-plate">Dr. Tariq Delwyn</div>

  <ul class="credentials">
    <li>BSc Med, MBBS (Hons 1) UNEC, MSc, FRACS (Oto-HNS)</li>
    <li>Consultant ENT/Head and Neck Surgeon</li>
    <li>Harbour Crest Cancer Centre</li>
    <li>Northgate Hospital and Coastal Valley Health District (CVHD)</li>
    <li>Senior Lecturer, University of Eastbridge (UEb) &amp; Westvale (UWV)</li>
  </ul>

  <ul class="practice-addresses">
    <li>Suite 208/46 Larkspur Road,</li>
    <li>Kellmont 2161</li>
    <li>19 Marlowe Highway, Ashbury Vale 2173</li>
    <li>35 Pemberton Street, Fernlea 2790</li>
  </ul>

  <div class="footer-band" role="img" aria-label="Abstract decorative footer in soft blue tones"></div>
</div>
</body>
</html>
```